Selka Marven Photography Business Card

I need a new business card/ possibly design to use for other marking materials ... I have included my logo below in a few different colors, but can also provide the logo in additional colors and sizes. I would love a card the expresses clean, simple and classy.

Target Market(s)

Portrait photography clients, child photography clients

Industry/Entity Type

Photographer

Contact Information for Business Card

Selka Marven Photography, Fernwick MA, www.selkamarvenphotography-demo.com
T. 555-203-1946 E. selkamarvenphoto@mailbox-demo.com

Colors
33b8a4
eea4c8
5c5c5c

Requirements
Must have
• I would like to include my logo on card.
Nice to have
• I also like the color brown as well as the choices below. I would like a simple, elegant card, something classy.

```html
<!DOCTYPE html>
<html lang="en">
<head>
<meta charset="utf-8">
<title>Selka Marven Photography – Business Card</title>
<link rel="stylesheet" href="https://fonts.googleapis.com/css2?family=Questrial&display=swap">
<style>
  :root {
    --teal: #58b8ad;
    --paper: #ffffff;
    --page: #ffffff;
    --edge: #e3e3e3;
  }
  * { margin: 0; padding: 0; box-sizing: border-box; }
  html, body {
    width: 1041px;
    height: 1200px;
    overflow: hidden;
    background: var(--page);
    font-family: "Questrial", "Century Gothic", sans-serif;
  }
  .canvas {
    position: relative;
    width: 1041px;
    height: 1200px;
  }
  .card {
    position: absolute;
  }
  .card-front {
    left: 170px;
    top: 49px;
    width: 701px;
    height: 507px;
    background: var(--teal);
  }
  .card-back {
    left: 170px;
    top: 658px;
    width: 701px;
    height: 389px;
    background: var(--paper);
    border: 1px solid var(--edge);
  }
  .line {
    position: absolute;
    left: 0;
    right: 0;
    text-align: center;
    white-space: nowrap;
  }
  .brand-name {
    letter-spacing: 0.12em;
  }
  .card-front .brand-name {
    top: 310px;
    font-size: 34px;
    color: var(--paper);
  }
  .card-back .brand-name {
    top: 86px;
    font-size: 25px;
    color: var(--teal);
  }
  .contact {
    color: var(--teal);
    font-size: 21px;
    line-height: 33px;
  }
  .contact-city { top: 170px; }
  .contact-online { top: 225px; }
  .contact-phone { top: 318px; }
</style>
</head>
<body>
  <main class="canvas">
    <section class="card card-front" aria-label="Card front">
      <p class="line brand-name">Selka Marven Photography</p>
    </section>

    <section class="card card-back" aria-label="Card back">
      <p class="line brand-name">Selka Marven Photography</p>
      <p class="line contact contact-city">Fernwick MA</p>
      <p class="line contact contact-online">
        www.selkamarvenphotography-demo.com<br>
        selkamarvenphoto@mailbox-demo.com
      </p>
      <p class="line contact contact-phone">555-203-1946</p>
    </section>
  </main>
</body>
</html>
```